Geschäftspapiere für Jobwebseite
Zielgruppe
Hier finden sie alle Informationen zu unserem Unternehmen:
https://www.heller-wandel.com
Aufgabenstellung
Gerne von den Farben angelehnt an die Website ein modernes Briefpapier gestalten.

```html
<!DOCTYPE html>
<html lang="de">
<head>
<meta charset="utf-8">
<title>Briefpapier – HELLER-WANDEL.de</title>
<link rel="stylesheet" href="https://fonts.googleapis.com/css2?family=Fira+Sans:wght@600;700&family=Quicksand:wght@500;600&display=swap">
<style>
  :root {
    --green-deep: #0a7a2c;
    --green: #14a03f;
    --green-light: #35c060;
    --ink: #2b2b2b;
    --paper: #fbfcfd;
    --stage: #f2f2f2;
  }
  * { box-sizing: border-box; margin: 0; padding: 0; }
  html, body { width: 1037px; height: 1200px; overflow: hidden; background: var(--stage); }
  .sheet {
    position: absolute; left: 54px; top: 0; width: 929px; height: 1200px;
    background: linear-gradient(150deg, var(--green-light), var(--green) 50%, var(--green-deep));
    overflow: hidden;
  }
  .sheet__field {
    position: absolute; left: 70px; top: 115px; right: 95px; bottom: 70px;
    background: var(--paper);
    border-radius: 40px;
    filter: blur(34px);
  }
  .letterhead {
    position: absolute; left: 114px; top: 132px;
    font-family: "Fira Sans", sans-serif; color: var(--ink);
  }
  .brand { display: flex; align-items: center; gap: 10px; }
  .brand__name { font-size: 29px; font-weight: 700; letter-spacing: 0.2px; }
  .brand__dot { width: 13px; height: 13px; border-radius: 50%; background: var(--green); }
  .sender { margin-top: 40px; font-size: 12.5px; font-weight: 700; }
  .contact {
    position: absolute; left: 618px; top: 140px; list-style: none;
    font-family: "Quicksand", sans-serif; font-weight: 600; font-size: 11.5px; color: var(--ink);
  }
  .contact__item { display: flex; align-items: center; gap: 9px; height: 25px; }
  .contact__icon {
    width: 19px; height: 19px; border-radius: 50%; background: var(--green);
    display: flex; align-items: center; justify-content: center;
  }
  .contact__icon svg { width: 11px; height: 11px; fill: #fff; }
  .footer {
    position: absolute; left: 196px; top: 1063px; display: flex;
    font-family: "Quicksand", sans-serif; font-weight: 600; font-size: 10.5px; line-height: 19px; color: var(--ink);
  }
  .footer__col { padding-right: 12px; }
  .footer__col + .footer__col { border-left: 1.5px solid var(--ink); padding-left: 10px; }
  .footer__col--tax { width: 90px; }
  .footer__col--bank { width: 160px; }
</style>
</head>
<body>
  <div class="sheet">
    <div class="sheet__field"></div>

    <header class="letterhead">
      <div class="brand">
        <span class="brand__name">HELLER-WANDEL.de</span>
        <span class="brand__dot"></span>
      </div>
      <p class="sender">Mira Lenzen / Talweg 18 / D-40210 Lindhausen</p>
    </header>

    <ul class="contact">
      <li class="contact__item">
        <span class="contact__icon"><svg viewBox="0 0 24 24"><path d="M6.6 10.8a15 15 0 0 0 6.6 6.6l2.2-2.2c.3-.3.7-.4 1-.2 1.1.4 2.3.6 3.6.6.6 0 1 .4 1 1V20c0 .6-.4 1-1 1C10.6 21 3 13.4 3 4c0-.6.4-1 1-1h3.5c.6 0 1 .4 1 1 0 1.3.2 2.5.6 3.6.1.3 0 .7-.2 1z"/></svg></span>
        0211.5550182
      </li>
      <li class="contact__item">
        <span class="contact__icon"><svg viewBox="0 0 24 24"><path d="M7 2h10a1 1 0 0 1 1 1v18a1 1 0 0 1-1 1H7a1 1 0 0 1-1-1V3a1 1 0 0 1 1-1zm1 3v12h8V5zm4 13.5a1 1 0 1 0 0 2 1 1 0 0 0 0-2z"/></svg></span>
        0170.5550947
      </li>
      <li class="contact__item">
        <span class="contact__icon"><svg viewBox="0 0 24 24"><path d="M2 11 22 3l-6 18-4-7-7-3zm6 0 5 2 3 5 3-11z"/></svg></span>
        info@lenzen-vermittlung.de
      </li>
      <li class="contact__item">
        <span class="contact__icon"><svg viewBox="0 0 24 24"><path d="M12 2a10 10 0 1 0 0 20 10 10 0 0 0 0-20zm0 2c.9 0 2.2 1.8 2.8 5H9.2C9.8 5.8 11.1 4 12 4zM4.3 11h3c-.1 1-.1 1.9 0 2h-3a8 8 0 0 1 0-2zm4.9 2v-2h5.6v2zm7.5 0v-2h3a8 8 0 0 1 0 2zM9.2 15h5.6c-.6 3.2-1.9 5-2.8 5s-2.2-1.8-2.8-5z"/></svg></span>
        lenzen-vermittlung.de
      </li>
    </ul>

    <footer class="footer">
      <div class="footer__col footer__col--tax">Steuer-Nr.<br>DE000123456</div>
      <div class="footer__col footer__col--bank">Bankverbindung:<br>Stadtsparkasse Lindhausen</div>
      <div class="footer__col">BIC LINDDEX1XXX<br>IBAN DE00 1234 0000 0000 5678 90</div>
    </footer>
  </div>
</body>
</html>
```